Dunmore County Assessor Canditate

We need a billboard ad for a political candidate Rosa Terwilliger who is running for Dunmore County Assessor in an upcoming election. Needs to be simple and to the point to get the people to see the name "Rosa Terwilliger" and what to vote for "Dunmore County Assessor" in Las Vegas, NV. Also the billboard visibility is best in the top side of the sign, so the information should be most prominent in the top right, middle, left sides.The size of the billboard is 14 ft Height X 48 ft Wide Also needs some bright colors that are noticable from a freeway viewed billboard.Designers - I need to have "Paid for by Rosa Terwilliger for Dunmore County Assessor" on the sign
I have uploaded a few headshots you can work with to create a design. Thank you,

http://rosaterwilliger.info/

Target Market(s)

Voters

Industry/Entity Type

Political

Requirements
Must have
• Name, what I am voting for, and some image that represents Las Vegas and/or Nevada

```html
<!DOCTYPE html>
<html lang="en">
<head>
<meta charset="utf-8">
<title>Rosa Terwilliger for Dunmore County Assessor – Billboard</title>
<link rel="stylesheet" href="https://fonts.googleapis.com/css2?family=Poppins:wght@600;700;900&family=Anton&family=Roboto:wght@500&display=swap">
<style>
  :root {
    --stage: #e9ecef;
    --board: #272727;
    --yellow: #f4f20a;
    --red: #f50505;
    --white: #ffffff;
    --photo-dark: #1e1e1e;
    --photo-light: #c9a871;
  }
  * { margin: 0; padding: 0; box-sizing: border-box; }
  html, body {
    width: 1200px;
    height: 583px;
    overflow: hidden;
    background: var(--stage);
  }
  .billboard {
    position: absolute;
    left: 0;
    top: 118px;
    width: 1200px;
    height: 347px;
    background: var(--board);
    overflow: hidden;
  }
  .candidate-photo {
    position: absolute;
    left: 0;
    top: 0;
    width: 300px;
    height: 100%;
    background: radial-gradient(ellipse 55% 70% at 45% 45%, var(--photo-light) 0%, #7a6650 45%, var(--photo-dark) 100%);
  }
  .candidate-name {
    position: absolute;
    left: 330px;
    right: 0;
    top: 10px;
    text-align: center;
    font-family: "Poppins", sans-serif;
    font-weight: 900;
    font-size: 78px;
    line-height: 1.1;
    color: var(--yellow);
    white-space: nowrap;
  }
  .office-banner {
    position: absolute;
    left: 307px;
    right: 0;
    top: 123px;
    height: 150px;
    background: var(--red);
    border-radius: 10px 0 0 10px;
    text-align: center;
  }
  .vote-for {
    display: block;
    padding-top: 10px;
    font-family: "Roboto", sans-serif;
    font-weight: 500;
    font-size: 42px;
    line-height: 1;
    color: var(--yellow);
  }
  .office-title {
    display: block;
    margin-top: 4px;
    font-family: "Anton", sans-serif;
    font-size: 80px;
    line-height: 1.05;
    color: var(--white);
    white-space: nowrap;
  }
  .disclaimer {
    position: absolute;
    left: 320px;
    right: 0;
    top: 296px;
    text-align: center;
    font-family: "Poppins", sans-serif;
    font-weight: 700;
    font-size: 22px;
    line-height: 1.2;
    color: var(--white);
    white-space: nowrap;
  }
  .disclaimer .lead { color: var(--yellow); }
</style>
</head>
<body>
  <section class="billboard">
    <div class="candidate-photo" role="img" aria-label="Headshot of candidate Rosa Terwilliger, smiling, with long blonde wavy hair and a dark blazer"></div>
    <h1 class="candidate-name">ROSA TERWILLIGER</h1>
    <div class="office-banner">
      <span class="vote-for">VOTE FOR</span>
      <span class="office-title">DUNMORE COUNTY ASSESSOR</span>
    </div>
    <p class="disclaimer"><span class="lead">Paid for by</span> Rosa Terwilliger for Dunmore County Assessor</p>
  </section>
</body>
</html>
```